Business Card Design Project

This is the first time we use our new logo. We need a business card that we can use both on our institutional corporate relationships and also that works for our staff that deals with consumers directly.

VELUNDA is a new company dedicated to empower consumers and to provide them with the best choices for specialized health care using the latest telemedicine technology (medicine at a distance via videoconference).

We want to print this cards in high quality materials and process. We will like designs that allow us to use UV spot varnish and other techniques that will differentiate us.

We are including Two different versions of Color logos. In addition we are including white over black background logos. Those can be used replacing the black for a color.

Please note this is the first time we will be creating any corporate materials with our new logo and colors.

Target Market(s)

34+ consumers of medium high and high socioeconomic levels.

Industry/Entity Type

Health

Requirements
Must have
• Our logo on its original colors
Should not have
• Any other graphical element or design that is not our logo

```html
<!DOCTYPE html>
<html lang="en">
<head>
<meta charset="utf-8">
<title>VELUNDA Business Card</title>
<link rel="stylesheet" href="https://fonts.googleapis.com/css2?family=Open+Sans:wght@400;600;700&display=swap">
<style>
  :root {
    --brand-blue: #1a5580;
    --brand-navy: #1d4f78;
    --text-grey: #555a60;
    --text-dark: #333333;
    --card-white: #ffffff;
    --page-bg: #ffffff;
    --pattern-light: #eef0f6;
    --pattern-soft: #f7f8fb;
    --card-shadow: rgba(0, 0, 0, 0.35);
  }
  * { margin: 0; padding: 0; box-sizing: border-box; }
  html, body {
    width: 1200px;
    height: 400px;
    overflow: hidden;
    background: var(--page-bg);
    font-family: "Open Sans", Arial, sans-serif;
  }
  .stage { position: relative; width: 1200px; height: 400px; }

  .card {
    position: absolute;
    top: 62px;
    width: 485px;
    height: 284px;
    background: var(--card-white);
    box-shadow: 3px 5px 7px var(--card-shadow);
    overflow: hidden;
  }
  .card-front { left: 57px; }
  .card-back { left: 646px; }

  /* Front */
  .header-wave { position: absolute; left: 0; top: 0; width: 485px; height: 284px; }
  .header-wave path { fill: var(--brand-blue); }
  .brand-dot {
    position: absolute; left: 30px; top: 30px;
    width: 36px; height: 36px;
    border: 3px solid var(--card-white);
    border-radius: 50%;
  }
  .brand-name-front {
    position: absolute; left: 90px; top: 39px;
    color: var(--card-white);
    font-weight: 700; font-size: 28px; letter-spacing: 1.5px; line-height: 1;
  }
  .person-name {
    position: absolute; left: 34px; top: 150px;
    color: var(--brand-blue);
    font-weight: 700; font-size: 20px; line-height: 1;
  }
  .person-role {
    position: absolute; left: 46px; top: 175px;
    color: var(--text-grey);
    font-size: 13px; line-height: 1;
  }
  .contact-list {
    position: absolute; left: 263px; top: 142px;
    list-style: none;
    color: var(--text-grey);
    font-size: 16px; line-height: 22px;
  }
  .contact-list li { display: flex; }
  .contact-label { width: 32px; font-weight: 700; }
  .website {
    position: absolute; left: 0; width: 485px; top: 232px;
    text-align: center;
    color: var(--brand-blue);
    font-weight: 700; font-size: 14px; line-height: 1;
  }
  .address {
    position: absolute; left: 0; width: 485px; top: 258px;
    text-align: center;
    color: var(--text-dark);
    font-size: 10.5px; line-height: 1;
  }

  /* Back */
  .pattern-field {
    position: absolute; inset: 0;
    background: radial-gradient(ellipse at center, var(--pattern-soft) 0%, var(--pattern-light) 100%);
  }
  .brand-mark-back {
    position: absolute; left: 92px; top: 118px;
    width: 46px; height: 46px;
    border-radius: 50%;
    background: var(--brand-navy);
  }
  .brand-name-back {
    position: absolute; left: 180px; top: 124px;
    color: var(--brand-navy);
    font-weight: 700; font-size: 38px; letter-spacing: 2.5px; line-height: 1;
  }
</style>
</head>
<body>
<main class="stage">
  <section class="card card-front" aria-label="Business card front">
    <svg class="header-wave" viewBox="0 0 485 284" aria-hidden="true">
      <path d="M0,0 H485 V56 C440,70 410,105 373,103 C330,101 300,78 243,78 C160,78 80,123 0,123 Z"/>
    </svg>
    <span class="brand-dot" aria-hidden="true"></span>
    <p class="brand-name-front">VELUNDA</p>

    <p class="person-name">RANDOM NAME</p>
    <p class="person-role">CEO</p>

    <ul class="contact-list">
      <li><span class="contact-label">P</span><span>123456789</span></li>
      <li><span class="contact-label">M</span><span>987654321</span></li>
      <li><span class="contact-label">E</span><span>name@website.com</span></li>
    </ul>

    <p class="website">www.yourwebsite.com</p>
    <p class="address">Address Line 1, Address Line 2, Zip 123456</p>
  </section>

  <section class="card card-back" aria-label="Business card back">
    <div class="pattern-field" role="img" aria-label="Soft pattern of light circles across the card back"></div>
    <span class="brand-mark-back" aria-hidden="true"></span>
    <p class="brand-name-back">VELUNDA</p>
  </section>
</main>
</body>
</html>
```